Refresh Application User Interface

Brindlecove wishes to update the look of its business applications. Two representative forms are shown below. Please note, we are not considering changes in functionality or usability. Our goal is a cleaner, more contemporary design.

Industry/Entity Type

Business

```html
<!DOCTYPE html>
<html lang="en">
<head>
<meta charset="utf-8">
<title>Brindlecove – Purchase Order</title>
<link href="https://fonts.googleapis.com/css2?family=Open+Sans:wght@400;600;700&display=swap" rel="stylesheet">
<style>
:root{
  --topbar:#2f3136;
  --ink:#3b3f45;
  --muted:#8f97a3;
  --link:#4a7fd4;
  --accent:#2f6fd6;
  --brand:#1c3f9e;
  --green:#4cae4c;
  --red:#e0334d;
  --band:#eceef1;
  --panel:#f6f6f7;
  --line:#d9dce1;
  --field:#ffffff;
  --field-line:#d6d9de;
}
*{box-sizing:border-box;margin:0;padding:0}
html,body{width:1200px;height:861px;overflow:hidden;background:#fff}
body{font-family:"Open Sans",sans-serif;color:var(--ink);position:relative}
.abs{position:absolute}
.topbar{left:0;top:0;width:1200px;height:54px;background:var(--topbar);color:#fff;font-size:18px}
.topbar .user{left:15px;top:14px}
.topbar .user b,.topbar .role b{font-weight:700}
.topbar .role{left:249px;top:14px}
.topbar .tools{right:20px;top:12px;display:flex;gap:18px;align-items:center}
.topbar .logout{color:#f04a5a}
.mainnav{left:0;top:76px;width:1200px;font-size:25px;color:var(--ink)}
.mainnav span{position:absolute;white-space:nowrap}
.mainnav .sep{color:#9aa0a8}
.mainnav .active{color:var(--accent);font-weight:700}
.brand{right:18px;top:78px;font-size:26px;font-weight:700;color:var(--brand);letter-spacing:1px}
.subnav{left:0;top:134px;font-size:21px;color:var(--muted)}
.subnav span{position:absolute;white-space:nowrap}
.subnav .active{color:var(--ink)}
.subnav-mark{left:27px;top:175px;width:63px;height:4px;background:var(--accent)}
.rule{left:0;top:180px;width:1200px;height:1px;background:var(--line)}
.page-title{left:26px;top:197px;font-size:24px}
.stepstrip{left:793px;top:207px;width:407px;height:29px;background:var(--band);font-size:12px}
.stepstrip .cur{left:0;top:0;width:102px;height:29px;background:#e1e3e7}
.stepstrip span{position:absolute;top:7px}
.dot{display:inline-block;width:13px;height:13px;border-radius:50%;background:var(--green);vertical-align:-2px;margin-right:10px;position:relative}
.dot::after{content:"";position:absolute;left:4px;top:2px;width:3px;height:6px;border:solid #fff;border-width:0 2px 2px 0;transform:rotate(45deg)}
.actionbar{left:0;top:236px;width:1200px;height:28px;background:var(--band);font-size:15px}
.actionbar .post{left:20px;top:4px;color:var(--link);display:flex;gap:8px;align-items:center}
.actionbar .act{top:4px;display:flex;gap:6px;align-items:center}
.label{font-size:15px;text-align:right;white-space:nowrap}
.value{font-size:13px}
.input{position:absolute;height:28px;border:1px solid var(--field-line);background:var(--field);font-size:12px;padding:5px 10px;white-space:nowrap;overflow:hidden}
.input.focus{border-color:var(--link)}
.panel{left:0;top:530px;width:1200px;height:281px;background:var(--panel)}
.sectabs{left:0;top:541px;font-size:16px;color:var(--muted)}
.sectabs span{position:absolute;white-space:nowrap}
.sectabs .active{color:var(--ink)}
.sec-mark{left:125px;top:567px;width:59px;height:4px;background:var(--accent)}
.select{position:absolute;height:25px;background:#fff;border:1px solid #e3e5e9;font-size:12px;padding:4px 9px}
.select::after{content:"";position:absolute;right:0;top:0;width:16px;height:23px;background:#e8eaed}
.select::before{content:"";position:absolute;right:4px;top:10px;border:4px solid transparent;border-top-color:#666;z-index:1}
.status{left:0;top:811px;width:1200px;height:50px;border-top:2px solid var(--line)}
.status .msg{left:550px;top:12px;font-size:20px;color:var(--muted)}
.status svg{position:absolute;top:10px}
</style>
</head>
<body>

<header class="abs topbar">
  <div class="abs user">Logged In As&nbsp; <b>Dana Hollis</b> ⚙</div>
  <div class="abs role">Current Role&nbsp; <b>administrator</b> ▾</div>
  <div class="abs tools">
    <svg width="26" height="30" viewBox="0 0 26 30" fill="none" stroke="#fff" stroke-width="1.6"><path d="M8 16V4a2 2 0 0 1 4 0v9m0-2a2 2 0 0 1 4 0v3m0-1a2 2 0 0 1 4 0v2m0 0a2 2 0 0 1 4 0v5c0 5-4 8-8 8h-2c-4 0-6-3-8-6l-3-5a2 2 0 0 1 3-2l2 3"/></svg>
    <svg width="32" height="28" viewBox="0 0 32 28" fill="none" stroke="#fff" stroke-width="1.6"><rect x="2" y="2" width="24" height="18"/><rect x="5" y="6" width="24" height="16"/><circle cx="27" cy="22" r="5" fill="#4cae4c" stroke="none"/><path d="M27 19v6M24 22h6" stroke="#fff"/></svg>
    <span>New Tab</span>
    <svg width="30" height="30" viewBox="0 0 30 30" fill="none" stroke="#fff" stroke-width="1.6"><circle cx="15" cy="15" r="13"/><path d="M11 11a4 4 0 1 1 5 4v3"/><circle cx="16" cy="22" r=".8" fill="#fff"/></svg>
    <svg width="30" height="30" viewBox="0 0 30 30" fill="none" stroke="#fff" stroke-width="1.6"><path d="M6 17v-3a9 9 0 0 1 18 0v3"/><rect x="4" y="16" width="5" height="8" rx="2"/><rect x="21" y="16" width="5" height="8" rx="2"/><path d="M24 24c0 3-4 4-8 4"/></svg>
    <svg width="30" height="30" viewBox="0 0 30 30" fill="none" stroke="#f04a5a" stroke-width="1.6"><path d="M18 3H4v24h14M12 15h16M23 10l5 5-5 5"/></svg>
    <span class="logout">Log Out</span>
  </div>
</header>

<nav class="abs mainnav">
  <span style="left:28px">Home</span><span class="sep" style="left:119px">|</span>
  <span style="left:150px">eSource</span><span class="sep" style="left:265px">|</span>
  <span class="active" style="left:296px">eBuy</span><span class="sep" style="left:378px">|</span>
  <span style="left:409px">eRequest</span><span class="sep" style="left:537px">|</span>
  <span style="left:568px">eStock</span><span class="sep" style="left:669px">|</span>
  <span style="left:700px">ePlan</span><span class="sep" style="left:785px">|</span>
  <span style="left:815px">Preferences</span>
</nav>
<div class="abs brand">BRINDLECOVE</div>

<nav class="abs subnav">
  <span class="active" style="left:27px">Orders</span>
  <span style="left:119px">Receipts</span>
  <span style="left:227px">Shipments</span>
  <span style="left:355px">Invoices</span>
  <span style="left:460px">Pricing</span>
  <span style="left:555px">Tables</span>
  <span style="left:642px">Reports</span>
  <span style="left:743px">Inquiries</span>
  <span style="left:853px">Periodic Tasks</span>
  <span style="left:1015px">Workflows</span>
</nav>
<div class="abs subnav-mark"></div>
<div class="abs rule"></div>

<h1 class="abs page-title" style="font-weight:400">Purchase Order</h1>
<div class="abs stepstrip">
  <div class="abs cur"></div>
  <span style="left:29px">Header</span>
  <span style="left:124px"><i class="dot"></i>Lines</span>
  <span style="left:232px">Changes</span>
  <span style="left:319px"><i class="dot"></i>Notes</span>
</div>

<div class="abs actionbar">
  <div class="abs post">
    <svg width="24" height="20" viewBox="0 0 24 20" fill="none" stroke="#4a7fd4" stroke-width="1.6"><rect x="1" y="2" width="19" height="14"/><path d="M1 7h19M5 11h7" /><circle cx="20" cy="15" r="4" fill="#4cae4c" stroke="none"/></svg>
    Post Order
  </div>
  <div class="abs act" style="left:816px;color:#8a919b">
    <svg width="20" height="20" viewBox="0 0 20 20" fill="none" stroke="#8a919b" stroke-width="1.8"><circle cx="8" cy="8" r="6"/><path d="M13 13l5 5"/></svg>search</div>
  <div class="abs act" style="left:904px;color:#8a919b">
    <svg width="18" height="18" viewBox="0 0 18 18" stroke="#8a919b" stroke-width="1.6"><path d="M9 1v16M1 9h16"/></svg>new</div>
  <div class="abs act" style="left:972px;color:var(--link)">
    <svg width="20" height="20" viewBox="0 0 20 20" fill="none" stroke="#4a7fd4" stroke-width="2.2"><path d="M6 3L2 7l4 4M2 7h9a6 6 0 0 1 0 12"/></svg>back</div>
  <div class="abs act" style="left:1043px;color:var(--green)">
    <svg width="22" height="20" viewBox="0 0 22 20" fill="none" stroke="#4cae4c" stroke-width="3"><path d="M2 10l6 6L20 3"/></svg>apply</div>
  <div class="abs act" style="left:1120px;color:var(--red)">
    <svg width="18" height="18" viewBox="0 0 18 18" stroke="#e0334d" stroke-width="3"><path d="M2 2l14 14M16 2L2 16"/></svg>delete</div>
</div>

<section class="ship-from">
  <div class="abs label" style="left:0;width:86px;top:275px">Order #</div>
  <div class="abs value" style="left:111px;top:277px">100159</div>

  <div class="abs label" style="left:0;width:86px;top:312px">Ship from</div>
  <div class="input" style="left:101px;top:308px;width:106px">1001</div>
  <div class="abs" style="left:215px;top:312px;color:var(--link)">/</div>
  <div class="input" style="left:230px;top:308px;width:34px">0</div>

  <div class="input focus" style="left:101px;top:345px;width:280px">Harborline Clinical Co.</div>
  <svg class="abs" style="left:392px;top:347px" width="24" height="24" viewBox="0 0 24 24" fill="none" stroke="#4a7fd4" stroke-width="1.3"><circle cx="12" cy="12" r="10.5"/><ellipse cx="12" cy="12" rx="4.5" ry="10.5"/><path d="M1.5 12h21M3 7h18M3 17h18"/></svg>

  <div class="abs label" style="left:0;width:86px;top:384px">Address</div>
  <div class="input" style="left:101px;top:382px;width:280px">14 Tidewater Rd</div>
  <div class="input" style="left:101px;top:418px;width:280px"></div>
  <div class="abs" style="left:399px;top:421px;font-size:15px;color:var(--link)">DPV Unconfirmed</div>

  <div class="abs label" style="left:0;width:86px;top:457px">City</div>
  <div class="input" style="left:101px;top:455px;width:204px">Eastbrook</div>
  <div class="abs label" style="left:322px;top:457px">State</div>
  <div class="input" style="left:371px;top:455px;width:42px">MA</div>
  <div class="abs" style="left:424px;top:457px;font-size:15px;color:var(--green);display:flex;gap:6px;align-items:center">
    <svg width="18" height="18" viewBox="0 0 18 18" fill="none" stroke="#4cae4c" stroke-width="1.6"><rect x="1" y="1" width="16" height="16" rx="3"/><path d="M5 9l3 3 5-6"/></svg>Accept</div>

  <div class="abs label" style="left:0;width:86px;top:494px">Zip</div>
  <div class="input" style="left:101px;top:491px;width:115px">01987-4410</div>
  <div class="abs label" style="left:231px;top:494px">Country</div>
  <div class="input" style="left:297px;top:491px;width:116px">US</div>
  <div class="abs" style="left:437px;top:494px;font-size:15px;color:var(--link);text-decoration:underline">Add Contact</div>
</section>

<section class="abs panel"></section>
<nav class="abs sectabs">
  <span style="left:26px">Order Info</span>
  <span class="active" style="left:125px">Shipping</span>
  <span style="left:213px">Payment</span>
  <span style="left:302px">Accounts</span>
  <span style="left:394px">Totals / Approval</span>
</nav>
<div class="abs sec-mark"></div>

<section class="shipping">
  <div class="abs label" style="left:0;width:132px;top:589px;font-size:14px">Receive At</div>
  <div class="select" style="left:142px;top:587px;width:151px">ALCH</div>
  <div class="abs label" style="left:0;width:132px;top:623px;font-size:14px">Carrier</div>
  <div class="select" style="left:142px;top:621px;width:151px">Swiftpost</div>
  <div class="abs label" style="left:0;width:132px;top:656px;font-size:14px">Express Service</div>
  <div class="select" style="left:142px;top:654px;width:151px"></div>
  <div class="abs label" style="left:0;width:132px;top:690px;font-size:14px">FOB</div>
  <div class="select" style="left:142px;top:688px;width:151px"></div>
  <div class="abs label" style="left:0;width:132px;top:724px;font-size:14px">Order Ship Rule</div>
  <div class="select" style="left:142px;top:722px;width:193px">Partials</div>
  <div class="abs label" style="left:0;width:132px;top:758px;font-size:14px">Line Ship Rule</div>
  <div class="select" style="left:142px;top:756px;width:193px">Partials</div>

  <div class="abs label" style="left:300px;width:132px;top:589px;font-size:14px">Request Date</div>
  <div class="select" style="left:442px;top:587px;width:151px;background:#fff">01/07/2018</div>
  <svg class="abs" style="left:568px;top:587px" width="25" height="25" viewBox="0 0 25 25"><rect width="25" height="25" fill="#e8eaed"/><rect x="5" y="6" width="15" height="13" fill="none" stroke="#666" stroke-width="1.4"/><path d="M5 10h15M8 13h2M12 13h2M16 13h1M8 16h2M12 16h2" stroke="#666" stroke-width="1.4"/></svg>
  <div class="abs label" style="left:300px;width:132px;top:623px;font-size:14px">Freight Terms</div>
  <div class="select" style="left:442px;top:621px;width:151px">Collect</div>
  <div class="abs label" style="left:300px;width:132px;top:656px;font-size:14px">Freight Calc</div>
  <div class="select" style="left:442px;top:654px;width:193px"></div>

  <div class="abs label" style="left:654px;top:587px;font-size:15px">Customer Ship To</div>
  <div class="input" style="left:784px;top:583px;width:105px;border-color:#e3e5e9"></div>
  <div class="abs" style="left:898px;top:586px;color:var(--link)">/</div>
  <div class="input" style="left:913px;top:583px;width:34px;border-color:#e3e5e9"></div>

  <svg class="abs" style="left:1109px;top:720px" width="24" height="31" viewBox="0 0 24 31" fill="none" stroke="#4a7fd4" stroke-width="1.3"><path d="M6 12V7a6 6 0 0 1 12 0v5"/><rect x="1" y="12" width="22" height="17"/><path d="M1 24h22"/><text x="12" y="22" font-size="8" text-anchor="middle" fill="#4a7fd4" stroke="none" font-family="Open Sans,sans-serif">0</text></svg>
</section>

<footer class="abs status">
  <svg style="left:15px" width="28" height="28" viewBox="0 0 28 28" fill="none" stroke="#4a7fd4" stroke-width="1.6"><path d="M20 8L9 19a3 3 0 0 0 4 4l12-12a5 5 0 0 0-7-7L6 16a7 7 0 0 0 10 10l9-9"/></svg>
  <svg style="left:60px" width="28" height="30" viewBox="0 0 28 30" fill="none" stroke="#4a7fd4" stroke-width="1.4"><path d="M19 27H2V2h14l5 5v8"/><path d="M6 9h9M6 13h9M6 17h6"/><circle cx="20" cy="21" r="4"/><path d="M23 24l4 4"/></svg>
  <svg style="left:102px" width="30" height="30" viewBox="0 0 30 30" fill="#4a7fd4" stroke="#4a7fd4" stroke-width="2"><circle cx="23" cy="6" r="4"/><circle cx="6" cy="15" r="4"/><circle cx="23" cy="25" r="4"/><path d="M6 15l17-9M6 15l17 10"/></svg>
  <svg style="left:154px" width="32" height="30" viewBox="0 0 32 30" fill="none" stroke="#4a7fd4" stroke-width="1.4"><rect x="2" y="7" width="28" height="21"/><path d="M11 7V3h10v4M2 14h28M9 12v5M23 12v5"/></svg>
  <svg style="left:207px" width="30" height="30" viewBox="0 0 30 30" fill="none" stroke="#555" stroke-width="1.6"><circle cx="15" cy="15" r="13"/><path d="M11 11a4 4 0 1 1 5 4v3"/><circle cx="16" cy="22" r=".8" fill="#555"/></svg>
  <div class="abs msg">Enter property values, and click Apply</div>
</footer>

</body>
</html>
```